Important Solar Energy Company Needs a Stationery Design

I need a modern, attractive, corporate stationary design (letter head and business card)
Attached Company Logo

Target Market(s)

Upmarket

Industry/Entity Type

Business

Colors
ec1f27
ffffff
757575
cbcbcb
000000

```html
<!DOCTYPE html>
<html lang="en">
<head>
<meta charset="utf-8">
<title>Solvanta Stationery</title>
<link href="https://fonts.googleapis.com/css2?family=Montserrat:wght@500;600&family=Roboto:wght@400;500;700&family=Lato:wght@400&display=swap" rel="stylesheet">
<style>
:root{
  --red:#ec1f27;
  --white:#ffffff;
  --grey:#757575;
  --light:#cbcbcb;
  --black:#000000;
  --ink:#222222;
  --body:#333333;
  --stage:#b3b3b3;
  --blush:#fadcdd;
  --sig-a:#dfe6f3;
  --sig-b:#c9d4ea;
}
*{box-sizing:border-box;margin:0;padding:0}
html,body{width:1200px;height:960px;overflow:hidden;background:var(--stage)}
.canvas{position:relative;width:1200px;height:960px;font-family:"Roboto",sans-serif;color:var(--ink)}
.card{position:absolute;width:272px;height:156px;background:var(--white);overflow:hidden;box-shadow:1px 1px 2px rgba(0,0,0,.25)}
.card--dark{background:var(--black);color:var(--white)}
.band{position:absolute;left:0;bottom:0;width:100%;height:11px;display:block}
.holder{position:absolute}
.holder__name{font-family:"Montserrat",sans-serif;font-weight:600;color:var(--red);font-size:12.5px;letter-spacing:.1px}
.holder__role{font-size:7px;margin-top:1px;color:inherit}
.contacts{position:absolute;font-size:8.3px;line-height:10.8px}
.contacts li{list-style:none;display:flex;align-items:center;gap:6px}
.contacts svg{width:7px;height:7px;fill:var(--red);flex:none}
.address{position:absolute;font-size:8.3px;line-height:10.8px}
.address--red{color:var(--red)}
.mark{position:absolute;border-radius:50%;background:var(--red)}
.brand{position:absolute;font-family:"Montserrat",sans-serif;font-weight:500;color:var(--ink);letter-spacing:2px;white-space:nowrap}
.card--dark .brand{color:var(--white)}
.rule{position:absolute;width:1px;background:var(--red)}

.sheet{position:absolute;top:388px;width:426px;height:550px;background:var(--white);overflow:hidden;box-shadow:1px 1px 2px rgba(0,0,0,.25);font-family:"Lato",sans-serif}
.sheet__wash{position:absolute;border-radius:50%;background:var(--blush)}
.sheet__body{position:absolute;font-size:7.4px;line-height:14.6px;color:var(--body)}
.sheet__body p{margin-bottom:14.6px}
.signature{width:98px;height:30px;background:linear-gradient(90deg,var(--sig-a),var(--sig-b));border-radius:3px;margin:4px 0 8px}
.sheet__contacts{position:absolute;font-size:5.2px;line-height:7px;border-left:1px solid var(--red);padding-left:7px}
.sheet__contacts li{list-style:none;display:flex;align-items:center;gap:4px}
.sheet__contacts svg{width:4.5px;height:4.5px;fill:var(--red)}
.sheet__contacts .strong{font-weight:700;font-family:"Roboto",sans-serif}
.sheet__footer{position:absolute;left:50px;bottom:14px;display:flex;gap:10px;font-size:4.8px;align-items:center;font-family:"Roboto",sans-serif}
.sheet__footer span{display:flex;align-items:center;gap:3px}
.sheet__footer svg{width:4.5px;height:4.5px;fill:var(--red)}
.sheet__footer .addr{border-left:1px solid var(--red);padding-left:5px;font-weight:500}
</style>
</head>
<body>
<svg width="0" height="0" style="position:absolute" aria-hidden="true">
  <symbol id="i-phone" viewBox="0 0 10 10"><path d="M1 3.5C1 2 3 1 5 1s4 1 4 2.5L7.5 4 7 3H3L2.5 4zM2.5 4.5h5L9 9H1z"/></symbol>
  <symbol id="i-mail" viewBox="0 0 10 10"><path d="M0 2h10v6H0zM1 3l4 3 4-3v-.4L5 5 1 2.6z" fill-rule="evenodd"/></symbol>
  <symbol id="i-web" viewBox="0 0 10 10"><path d="M5 0a5 5 0 1 0 0 10A5 5 0 0 0 5 0zm0 1a4 4 0 0 1 0 8 4 4 0 0 1 0-8zM1 4.5h8v1H1zM4.5 1h1v8h-1z"/></symbol>
  <symbol id="band" viewBox="0 0 272 11" preserveAspectRatio="none"><polygon points="0,0 183,0 179,11 0,11" fill="#ec1f27"/><polygon points="187,0 272,0 272,11 183,11" fill="#000"/></symbol>
</svg>

<main class="canvas">

  <section class="card" style="left:22px;top:27px">
    <div class="mark" style="left:-8px;top:45px;width:102px;height:102px"></div>
    <div class="holder" style="left:148px;top:20px"><div class="holder__name">Marina Castell</div><div class="holder__role">Director</div></div>
    <ul class="contacts" style="left:148px;top:79px">
      <li><svg><use href="#i-phone"/></svg>+00 41 555 0172</li>
      <li><svg><use href="#i-mail"/></svg>hello@solvanta.com</li>
      <li><svg><use href="#i-web"/></svg>www.solvanta.com</li>
    </ul>
    <div class="address" style="left:148px;top:118px">Marlow Lane, Eastbrook<br>City Name, USA 0000</div>
  </section>

  <section class="card" style="left:314px;top:27px">
    <div class="holder" style="left:25px;top:25px"><div class="holder__name">Marina Castell</div><div class="holder__role">Director</div></div>
    <ul class="contacts" style="left:25px;top:71px">
      <li><svg><use href="#i-phone"/></svg>+00 41 555 0172</li>
      <li><svg><use href="#i-mail"/></svg>hello@solvanta.com</li>
      <li><svg><use href="#i-web"/></svg>www.solvanta.com</li>
    </ul>
    <div class="address" style="left:25px;top:109px">Marlow Lane, Eastbrook<br>City Name, USA 0000</div>
    <div class="mark" style="left:147px;top:104px;width:24px;height:24px"></div>
    <div class="brand" style="left:178px;top:111px;font-size:9px">SOLVANTA</div>
    <svg class="band"><use href="#band"/></svg>
  </section>

  <section class="card" style="left:607px;top:27px">
    <div class="mark" style="left:48px;top:61px;width:48px;height:48px"></div>
    <div class="brand" style="left:24px;top:118px;font-size:11px">SOLVANTA</div>
    <div class="rule" style="left:138px;top:34px;height:90px"></div>
    <div class="holder" style="left:151px;top:32px"><div class="holder__name">Marina Castell</div><div class="holder__role">Director</div></div>
    <ul class="contacts" style="left:151px;top:72px">
      <li><svg><use href="#i-phone"/></svg>+00 41 555 0172</li>
      <li><svg><use href="#i-mail"/></svg>hello@solvanta.com</li>
      <li><svg><use href="#i-web"/></svg>www.solvanta.com</li>
    </ul>
    <div class="address" style="left:151px;top:110px">Marlow Lane, Eastbrook<br>City Name, USA 0000</div>
    <svg class="band"><use href="#band"/></svg>
  </section>

  <section class="card" style="left:900px;top:27px">
    <div class="mark" style="left:98px;top:27px;width:73px;height:73px"></div>
    <div class="brand" style="left:0;width:272px;text-align:center;top:112px;font-size:17px">SOLVANTA</div>
    <svg class="band"><use href="#band"/></svg>
  </section>

  <section class="card card--dark" style="left:22px;top:207px">
    <div class="mark" style="left:-8px;top:45px;width:102px;height:102px"></div>
    <div class="holder" style="left:146px;top:15px"><div class="holder__name">Marina Castell</div><div class="holder__role">Director</div></div>
    <ul class="contacts" style="left:146px;top:78px">
      <li><svg><use href="#i-phone"/></svg>+00 41 555 0172</li>
      <li><svg><use href="#i-mail"/></svg>hello@solvanta.com</li>
      <li><svg><use href="#i-web"/></svg>www.solvanta.com</li>
    </ul>
    <div class="address" style="left:146px;top:116px">Marlow Lane, Eastbrook<br>City Name, USA 0000</div>
  </section>

  <section class="card" style="left:314px;top:207px">
    <div class="holder" style="left:152px;top:14px"><div class="holder__name">Marina Castell</div><div class="holder__role">Director</div></div>
    <ul class="contacts" style="left:21px;top:78px">
      <li><svg><use href="#i-phone"/></svg>+00 41 555 0172</li>
      <li><svg><use href="#i-mail"/></svg>hello@solvanta.com</li>
      <li><svg><use href="#i-web"/></svg>www.solvanta.com</li>
    </ul>
    <div class="address address--red" style="left:21px;top:114px">Marlow Lane, Eastbrook<br>City Name, USA 0000</div>
    <div class="mark" style="left:185px;top:75px;width:40px;height:40px"></div>
    <div class="brand" style="left:165px;top:122px;font-size:10px">SOLVANTA</div>
  </section>

  <section class="card" style="left:607px;top:207px">
    <div class="mark" style="left:23px;top:54px;width:47px;height:47px"></div>
    <div class="brand" style="left:86px;top:67px;font-size:19px">SOLVANTA</div>
  </section>

  <section class="card" style="left:898px;top:207px;width:276px;height:158px">
    <div class="mark" style="left:23px;top:54px;width:47px;height:47px"></div>
    <div class="brand" style="left:87px;top:68px;font-size:19px">SOLVANTA</div>
    <svg class="band"><use href="#band"/></svg>
  </section>

  <article class="sheet" style="left:136px;width:425px">
    <div class="sheet__wash" style="left:-76px;top:357px;width:229px;height:229px"></div>
    <div class="mark" style="left:63px;top:21px;width:38px;height:38px"></div>
    <div class="brand" style="left:43px;top:66px;font-size:9.5px">SOLVANTA</div>
    <ul class="sheet__contacts" style="left:302px;top:29px">
      <li><svg><use href="#i-phone"/></svg>+00 41 555 0172</li>
      <li><svg><use href="#i-mail"/></svg>hello@solvanta.com</li>
      <li><svg><use href="#i-web"/></svg>www.solvanta.com</li>
      <li style="margin-top:4px" class="strong">Marlow Lane, Eastbrook</li>
      <li class="strong">City Name, USA 0000</li>
    </ul>
    <div class="sheet__body" style="left:40px;top:96px;width:338px">
      <p>Lorem Ipsum is simply</p>
      <p>dummy text of the printing and typesetting industry. Lorem Ipsum has been the industry's standard dummy text ever since the 1500s, when an unknown printer took a galley of type and scrambled it to make a type specimen book. It has survived not only five centuries, but also the leap into electronic typesetting, remaining essentially unchanged.</p>
      <p>It is a long established fact that a reader will be distracted by the readable content of a page when looking at its layout. The point of using Lorem Ipsum is that it has a more-or-less normal distribution of letters, as opposed to using 'Content here, content here', making it look like readable English. Many desktop publishing packages and web page editors now use Lorem Ipsum as their default model text, and a search for 'lorem ipsum' will uncover many web sites still in their infancy. Various versions have</p>
      <p>Contrary to popular belief, Lorem Ipsum is not simply random text. It has roots in a piece of classical Latin literature from 45 BC, making it over 2000 years old. Tomas Verhalen, a Latin professor at Ardent-Hollis College in Vermont, looked up one of the more obscure Latin words, consectetur, from a Lorem Ipsum passage, and going through the cites of the word in classical literature, discovered the undoubtable source. Lorem Ipsum comes from sections 1.10.32 and 1.10.33 of "de Lumine Rerum et Ordine" (The Light of Things and Order) by Varrius, written in 45 BC. This book</p>
      <div style="margin-top:-6px">Lorem Ipsum</div>
      <div class="signature" role="img" aria-label="Handwritten signature"></div>
      <div>Lorem Ipsum is a dummy</div>
    </div>
  </article>

  <article class="sheet" style="left:610px">
    <div class="sheet__wash" style="left:-76px;top:357px;width:229px;height:229px"></div>
    <div class="mark" style="left:130px;top:18px;width:35px;height:35px"></div>
    <div class="brand" style="left:176px;top:28px;font-size:14px">SOLVANTA</div>
    <div class="sheet__body" style="left:41px;top:70px;width:342px">
      <p>Lorem Ipsum is simply</p>
      <p>dummy text of the printing and typesetting industry. Lorem Ipsum has been the industry's standard dummy text ever since the 1500s, when an unknown printer took a galley of type and scrambled it to make a type specimen book. It has survived not only five centuries, but also the leap into electronic typesetting, remaining essentially unchanged.</p>
      <p>It is a long established fact that a reader will be distracted by the readable content of a page when looking at its layout. The point of using Lorem Ipsum is that it has a more-or-less normal distribution of letters, as opposed to using 'Content here, content here', making it look like readable English. Many desktop publishing packages and web page editors now use Lorem Ipsum as their default model text, and a search for 'lorem ipsum' will uncover many web sites still in their infancy. Various versions have</p>
      <p>Contrary to popular belief, Lorem Ipsum is not simply random text. It has roots in a piece of classical Latin literature from 45 BC, making it over 2000 years old. Tomas Verhalen, a Latin professor at Ardent-Hollis College in Vermont, looked up one of the more obscure Latin words, consectetur, from a Lorem Ipsum passage, and going through the cites of the word in classical literature, discovered the undoubtable source. Lorem Ipsum comes from sections 1.10.32 and 1.10.33 of "de Lumine Rerum et Ordine" (The Light of Things and Order) by Varrius, written in 45 BC. This book</p>
      <div style="margin-top:-6px">Lorem Ipsum</div>
      <div class="signature" role="img" aria-label="Handwritten signature"></div>
      <div>Lorem Ipsum is a dummy</div>
    </div>
    <div class="sheet__footer">
      <span><svg><use href="#i-phone"/></svg>+00 41 555 0172</span>
      <span><svg><use href="#i-mail"/></svg>hello@solvanta.com</span>
      <span><svg><use href="#i-web"/></svg>www.solvanta.com</span>
      <span class="addr">Marlow Lane, Eastbrook, City Name, USA 0000</span>
    </div>
  </article>

</main>
</body>
</html>
```